Podcast cover art (not a logo)

I’m launching an audio-only podcast for parents of neurodivergent children. The podcast is meant to feel like a calm, trusted professional voice — not a brand or a performance.

Style direction:
--Clean and minimal
--Calm and grounded
--Professional, not playful
--Nothing flashy, loud, or busy
--No cartoon imagery

Content on the cover:
--Podcast title: Under the Quiet Surface
--Subtitle or tagline: Supporting Neurodivergent Kids with Science, Not Shame (or Understanding Neurodivergent Kids)
--No episode numbers, no dates

Design preferences:
--Text-forward design
--Neutral or soft colors (muted blues, grays, off-whites)
--High contrast for readability at small sizes
--Simple, timeless font

What I do NOT want:
--A logo or branding system
--Illustrations of children or families
--Bright colors or playful graphics
--Trendy fonts or visual effects

Technical requirements:
--Square image
--3000 × 3000 pixels
--RGB color mode
--JPEG or PNG
--File size under 500 KB

Deliverables:
--Final cover art file
--Optional: one or two alternate background color versions

```html
<!DOCTYPE html>
<html lang="en">
<head>
<meta charset="utf-8">
<title>Under the Quiet Surface — Podcast Cover</title>
<link rel="stylesheet" href="https://fonts.googleapis.com/css2?family=League+Gothic&family=Source+Sans+3:wght@600&display=swap">
<style>
  :root {
    --cover-ground: #2b4763;
    --title-offwhite: #f3efe7;
    --tagline-sand: #e6dcc8;
    --tone-mist: #b9cfdf;
    --tone-fog: #d3dbe1;
    --tone-sky: #a7c0d4;
    --tone-stone: #c8ccce;
    --tone-slate: #9fb4c6;
    --tone-pearl: #dde4e8;
    --tone-haze: #b2c6d3;
  }
  html, body {
    margin: 0;
    padding: 0;
    width: 1200px;
    height: 1200px;
    overflow: hidden;
    background: var(--cover-ground);
  }
  .cover {
    display: block;
    width: 1200px;
    height: 1200px;
  }
  .title-lead {
    font-family: "League Gothic", "Oswald", sans-serif;
    font-size: 196px;
    fill: var(--title-offwhite);
  }
  .title-main {
    font-family: "League Gothic", "Oswald", sans-serif;
    font-size: 332px;
  }
  .tagline {
    font-family: "Source Sans 3", "Helvetica Neue", sans-serif;
    font-weight: 600;
    font-size: 54px;
    fill: var(--tagline-sand);
  }
  .t-mist  { fill: var(--tone-mist); }
  .t-fog   { fill: var(--tone-fog); }
  .t-sky   { fill: var(--tone-sky); }
  .t-stone { fill: var(--tone-stone); }
  .t-slate { fill: var(--tone-slate); }
  .t-pearl { fill: var(--tone-pearl); }
  .t-haze  { fill: var(--tone-haze); }
</style>
</head>
<body>
<svg class="cover" viewBox="0 0 1200 1200" xmlns="http://www.w3.org/2000/svg" role="img" aria-label="Under the Quiet Surface — Understanding Neurodivergent Kids">
  <rect class="cover-ground" width="1200" height="1200" fill="var(--cover-ground)"/>

  <text class="title-lead" x="164" y="484" textLength="872" lengthAdjust="spacing">UNDER THE QUIET</text>

  <text class="title-main" x="164" y="780" textLength="872" lengthAdjust="spacing"><tspan class="t-mist">S</tspan><tspan class="t-fog">U</tspan><tspan class="t-sky">R</tspan><tspan class="t-stone">F</tspan><tspan class="t-slate">A</tspan><tspan class="t-pearl">C</tspan><tspan class="t-haze">E</tspan></text>

  <text class="tagline" x="164" y="866" textLength="872" lengthAdjust="spacing">Understanding Neurodivergent Kids</text>
</svg>
</body>
</html>
```